依頼詳細
会社のロゴを添付ファイルに添付しますのでロゴを用いた名刺デザインを作成していただきたいです。
お客様が会社になるため渡すときに恥ずかしくない名刺にしていただきたいです。
よろしくお願いいたします。
記載項目
表面:会社名、住所、メールアドレス、電話番号、役職、名前(ローマ字と漢字)、ロゴ
裏面:ロゴ、写真
希望イメージ
シンプル 複雑
単色 カラフル
暗い 明るい
日常 高級
遊び心 厳粛
未来的 伝統的
女性的 男性的
希望する色
青系、無彩色系
納品ファイル
• 高解像度JPG (.jpg)
• イラストレーター形式 (.ai)
補足説明

```html
<!DOCTYPE html>
<html lang="ja">
<head>
<meta charset="utf-8">
<title>名刺 表面</title>
<link rel="stylesheet" href="https://fonts.googleapis.com/css2?family=Cutive+Mono&family=Noto+Sans+JP:wght@300;400&family=Noto+Serif+JP:wght@300;400&display=swap">
<style>
  :root {
    --paper: #ffffff;
    --ink: #2e2e2e;
    --ink-soft: #555555;
  }
  html, body {
    margin: 0;
    padding: 0;
    overflow: hidden;
    background: var(--paper);
  }
  .card {
    position: relative;
    width: 707px;
    height: 1200px;
    background: var(--paper);
    color: var(--ink);
    overflow: hidden;
  }
  .brand {
    position: absolute;
    left: 95px;
    top: 112px;
    width: 210px;
    text-align: center;
  }
  .brand-dot {
    display: block;
    width: 58px;
    height: 58px;
    margin: 0 auto 18px;
    border-radius: 50%;
    background: var(--ink);
  }
  .brand-name {
    font-family: "Noto Sans JP", sans-serif;
    font-weight: 300;
    font-size: 52px;
    letter-spacing: 10px;
    line-height: 1;
    color: var(--ink);
  }
  .role {
    position: absolute;
    left: 78px;
    top: 452px;
    font-family: "Noto Serif JP", serif;
    font-weight: 300;
    font-size: 29px;
    letter-spacing: 4px;
    color: var(--ink-soft);
  }
  .person-name {
    position: absolute;
    left: 74px;
    top: 530px;
    font-family: "Noto Serif JP", serif;
    font-weight: 300;
    font-size: 58px;
    letter-spacing: 14px;
    line-height: 1;
    color: var(--ink);
  }
  .person-name .given { margin-left: 30px; }
  .person-roman {
    position: absolute;
    left: 80px;
    top: 636px;
    font-family: "Noto Sans JP", sans-serif;
    font-weight: 300;
    font-size: 26px;
    letter-spacing: 3px;
    color: var(--ink-soft);
    display: flex;
    gap: 90px;
  }
  .company {
    position: absolute;
    left: 78px;
    top: 852px;
    font-family: "Noto Serif JP", serif;
    font-weight: 300;
    font-size: 34px;
    letter-spacing: 4px;
    color: var(--ink);
  }
  .contact {
    position: absolute;
    left: 78px;
    top: 944px;
    margin: 0;
    padding: 0;
    list-style: none;
    font-family: "Cutive Mono", "Noto Serif JP", monospace;
    font-size: 29px;
    line-height: 49px;
    letter-spacing: 2px;
    color: var(--ink);
    white-space: nowrap;
  }
</style>
</head>
<body>
  <main class="card">
    <div class="brand">
      <span class="brand-dot"></span>
      <div class="brand-name">lumen</div>
    </div>

    <div class="role">代表取締役</div>
    <div class="person-name"><span class="family">森田</span><span class="given">悠真</span></div>
    <div class="person-roman"><span>MORITA</span><span>YUMA</span></div>

    <div class="company">株式会社ルーメン</div>
    <ul class="contact">
      <li class="address">神奈川県横浜市西区0丁目0番地0−0</li>
      <li class="phone">000-0000-0000</li>
      <li class="email">yuma@lumen-corp.site</li>
    </ul>
  </main>
</body>
</html>
```